Astrology Reading Website to attract clients

I need a website for my astrology practice. My business name is Willow Tide Astrology. I will need a page the following pages: About, Readings, Booking, Contact, and Blog. I will need full figma or figma-like mockups of pages along with assets. I will need both desktop and mobile designs.
I like creams, dark blues and greens. I am fine with planets or other astrology symbolism.

Target Market(s)

new age, spiritual

Industry/Entity Type

Holistic, spiritual

Number of Pages Required

3 page

Colors
0054AA
0677BA
7BADD7
CADEEF
E8F1F8

Requirements
Nice to have
• calm and grounded backgrounds

```html
<!DOCTYPE html>
<html lang="en">
<head>
<meta charset="UTF-8">
<title>Willow Tide Astrology</title>
<link href="https://fonts.googleapis.com/css2?family=Outfit:wght@400;500;600&family=Poppins:wght@400;500;600&display=swap" rel="stylesheet">
<style>
:root{
  --navy:#0b1a2f;
  --navy-deep:#081425;
  --card:#10264a;
  --card-soft:#132b50;
  --cream:#f6efa8;
  --cream-text:#f3e9a0;
  --white:#ffffff;
  --muted:#c9d3e2;
  --dark-text:#0b1a2f;
}
*{margin:0;padding:0;box-sizing:border-box}
html,body{width:1200px;height:4938px;overflow:hidden}
body{background:var(--navy);font-family:'Poppins',sans-serif;color:var(--white);position:relative}
.abs{position:absolute}
h1,h2,h3,.heading{font-family:'Outfit',sans-serif;font-weight:500}
.eyebrow{font-family:'Poppins',sans-serif;font-size:14px;color:var(--cream-text);text-transform:uppercase;letter-spacing:.2px}
.center{left:0;width:1200px;text-align:center}
.section-title{font-size:46px;color:var(--white);font-weight:500}
.rule{height:3px;width:56px;background:var(--cream);left:572px}
.lead{font-size:13.5px;line-height:27px;color:var(--muted);left:170px;width:860px;text-align:center}
.btn{background:var(--cream);color:var(--dark-text);border-radius:30px;font-size:15px;font-weight:500;display:flex;align-items:center;justify-content:center}

/* header & hero */
.hero{left:0;top:0;width:1200px;height:744px;background:radial-gradient(ellipse at 70% 45%,#183154 0%,#0d1f38 55%,#0a1930 100%)}
.logo{left:69px;top:32px;font-family:'Outfit',sans-serif;font-size:27px;font-weight:500;color:var(--white)}
.nav a{position:absolute;top:42px;font-size:13px;color:var(--white);text-decoration:none;text-transform:uppercase}
.nav a.active{color:var(--cream-text)}
.nav a.active::before{content:"";position:absolute;left:-4px;right:-4px;top:-18px;height:2px;background:var(--cream)}
.contact-btn{left:981px;top:26px;width:156px;height:44px;font-size:13px;text-transform:uppercase}
.hero-title{left:135px;top:278px;font-size:54px;line-height:66px;color:var(--white)}
.hero-text{left:140px;top:431px;width:460px;font-size:14px;line-height:26px;color:var(--white)}
.hero-btn{left:139px;top:512px;width:157px;height:48px}
.wheel{left:636px;top:134px;width:494px;height:494px;border-radius:50%;border:2px solid #9fb0c9;background:radial-gradient(circle,#1d3558 0%,#13294a 60%,#0f2342 100%)}
.dots{left:572px;top:675px;display:flex;gap:5px}
.dots span{width:11px;height:11px;border-radius:50%;background:#8d98a9}
.dots span:first-child{background:var(--white)}

/* about */
.about-frame{left:69px;top:853px;width:287px;height:447px;background:#15305a}
.about-img{left:100px;top:883px;width:443px;height:379px;background:radial-gradient(circle at 40% 45%,#c98a4a 0%,#5b3a2c 22%,#1a2237 55%,#0a0f1c 100%)}
.about-sq{width:47px;height:48px;background:var(--cream);left:421px}
.about-eyebrow{left:620px;top:883px;display:flex;align-items:center;gap:14px}
.about-eyebrow::after{content:"";width:56px;height:2px;background:var(--cream)}
.about-title{left:618px;top:905px;font-size:46px}
.about-text{left:615px;top:997px;width:518px;font-size:14px;line-height:26.6px;color:var(--muted);text-align:justify}
.about-btn{left:616px;top:1203px;width:153px;height:44px}

/* services */
.services{left:0;top:1428px;width:1200px;height:892px;background:radial-gradient(ellipse at 80% 10%,#1a2d48 0%,#0b1a2f 50%),var(--navy)}
.service{width:344px;height:197px;background:var(--card)}
.service .icon{left:28px;top:50px;width:96px;height:96px;border-radius:50%;border:1.5px dashed #8fa0ba;display:flex;align-items:center;justify-content:center}
.service .icon span{width:44px;height:44px;border-radius:50%;background:var(--cream);opacity:.9}
.service h3{position:absolute;left:141px;top:38px;font-size:21px}
.service .bar{left:141px;top:72px;width:46px;height:2px;background:var(--cream)}
.service p{position:absolute;left:141px;top:88px;width:185px;font-size:12.5px;line-height:22px;color:var(--muted)}
.service .more{left:141px;top:142px;font-size:11px;color:var(--cream-text);text-decoration:underline}

/* reviews */
.review{width:285px;height:273px;background:var(--card)}
.review p{position:absolute;left:33px;top:30px;width:220px;font-size:12px;line-height:24.5px;color:var(--muted);text-align:justify}
.review .name{left:32px;top:200px;font-size:15px;font-weight:500}
.review .role{left:32px;top:224px;font-size:10.5px;color:var(--muted)}
.avatar{left:193px;top:157px;width:50px;height:50px;border-radius:50%;background:linear-gradient(160deg,#e9ddd0,#b8a79a);border:2px solid #2a4268}
.quote{left:232px;top:181px;width:24px;height:24px;border-radius:50%;background:var(--cream);color:var(--dark-text);font-family:'Outfit',sans-serif;font-size:22px;font-weight:600;line-height:30px;text-align:center}
.arrow{width:36px;height:36px;border-radius:50%;display:flex;align-items:center;justify-content:center}
.arrow.light{background:#e7e9ee}
.arrow.cream{background:var(--cream)}

/* cta */
.cta{left:0;top:3077px;width:1200px;height:489px;background:radial-gradient(ellipse at 78% 40%,#3a4c72 0%,#23345a 35%,#141f3e 100%)}
.cta-title{top:3228px;font-size:48px;line-height:58px}
.cta-btn{left:478px;top:3413px;width:244px;height:47px;font-size:16px}

/* blogs */
.blog{width:275px;height:472px;background:var(--card)}
.blog .photo{left:5px;top:4px;width:265px;height:218px}
.blog .date{left:157px;top:200px;width:100px;height:26px;background:var(--cream);color:var(--dark-text);font-size:9.5px;font-weight:500;display:flex;align-items:center;justify-content:center;gap:5px}
.blog h3{position:absolute;left:28px;top:258px;width:230px;font-family:'Poppins',sans-serif;font-size:15.5px;font-weight:500;line-height:26px}
.blog p{position:absolute;left:28px;top:318px;width:230px;font-size:12px;line-height:21.5px;color:var(--muted)}
.blog .read{left:28px;top:395px;width:78px;height:24px;font-size:10px}

/* footer */
.footer{left:0;top:4515px;width:1200px;height:423px;background:radial-gradient(ellipse at 8% 0%,#1b3150 0%,#0b1a2f 40%)}
.f-logo{left:67px;top:4608px;font-family:'Outfit',sans-serif;font-size:23px;font-weight:500;color:var(--cream-text)}
.f-text{left:69px;top:4662px;width:270px;font-size:12px;line-height:25.5px;color:var(--muted);text-align:justify}
.social{left:78px;top:4812px;display:flex;gap:16px}
.social span{width:14px;height:14px;border-radius:50%;background:var(--cream)}
.f-head{font-family:'Outfit',sans-serif;font-size:18px;font-weight:500;top:4608px}
.f-links{left:400px;top:4670px;list-style:none}
.f-links li{font-size:13px;line-height:26px;display:flex;align-items:center;gap:20px}
.f-links li::before{content:"";width:5px;height:5px;border-radius:50%;background:var(--white)}
.c-row{left:572px;display:flex;gap:18px;font-size:13px;line-height:18px}
.c-icon{width:22px;height:22px;border-radius:50%;background:#1d3a63;display:flex;align-items:center;justify-content:center;flex-shrink:0;margin-top:4px}
.newsletter{left:840px;top:4648px;width:293px;height:164px;background:#13294c}
.newsletter h3{position:absolute;left:31px;top:26px;font-size:18px}
.newsletter p{position:absolute;left:31px;top:58px;width:220px;font-size:12.5px;line-height:19px}
.news-field{left:30px;top:112px;width:233px;height:28px;border:1px solid #8a97ad;display:flex;align-items:center;justify-content:space-between}
.news-field span{font-size:9px;color:var(--muted);padding-left:17px}
.news-field b{width:62px;height:22px;background:var(--cream);margin-right:3px;display:flex;align-items:center;justify-content:center}
.copy{left:0;top:4888px;width:1200px;height:50px;border-top:1px solid #1f3658;font-size:11px;display:flex;align-items:center;justify-content:center;color:var(--white)}
</style>
</head>
<body>

<!-- Header & hero -->
<section class="hero abs">
  <div class="logo abs">Willow Tide Astrology</div>
  <nav class="nav">
    <a class="active" style="left:496px">Home</a>
    <a style="left:584px">About</a>
    <a style="left:678px">Readings</a>
    <a style="left:795px">Booking</a>
    <a style="left:906px">Blog</a>
  </nav>
  <div class="btn contact-btn abs">Contact Us</div>

  <div class="eyebrow abs" style="left:135px;top:243px;font-size:17px">Willow Tide Astrology</div>
  <h1 class="hero-title abs">Ultimate Guide To<br>Astrology</h1>
  <p class="hero-text abs">Lorem ipsum dolor sit amet, consectetur adipiscing elit, sed do eiusmod tempor incididunt ut labore et dolore magna aliqua.</p>
  <div class="btn hero-btn abs">Learn More</div>
  <div class="wheel abs" role="img" aria-label="Zodiac wheel with the twelve signs and constellations around a central star"></div>
  <div class="dots abs"><span></span><span></span><span></span><span></span></div>
</section>

<!-- About -->
<div class="about-frame abs"></div>
<div class="about-img abs" role="img" aria-label="Figure silhouetted against a sky of planets and a ringed gas giant"></div>
<div class="about-sq abs" style="top:836px"></div>
<div class="about-sq abs" style="top:1266px"></div>
<div class="about-eyebrow eyebrow abs" style="font-size:13px">Who We Are</div>
<h2 class="about-title abs section-title">About Us</h2>
<p class="about-text abs">Lorem ipsum dolor sit amet, consectetur adipiscing elit. Etiam ullamcorper ut nibh eu lacinia. Maecenas lobortis convallis justo, at ultricies massa. Nunc quam diam, cursus eleifend gravida ac, ornare sit amet risus. Morbi finibus augue ligula, ut tristique neque rhoncus in. Vivamus condimentum, ex sit amet convallis pharetra, ante ante sagittis tellus, et aliquet erat justo quis nisl. Donec sed arcu eget sapien laoreet accumsan eget sed libero. Morbi non lacinia elit.</p>
<div class="btn about-btn abs">Read More</div>

<!-- Services -->
<section class="services abs">
  <div class="eyebrow abs center" style="top:86px">What We Do</div>
  <h2 class="section-title abs center" style="top:107px">Our Services</h2>
  <div class="rule abs" style="top:190px"></div>
  <p class="lead abs" style="top:232px">Lorem ipsum dolor sit amet, consectetur adipiscing elit. Etiam ullamcorper ut nibh eu lacinia. Maecenas lobortis convallis justo, at ultricies massa. Nunc quam diam, cursus eleifend gravida ac, ornare sit amet risus.</p>

  <div class="service abs" style="left:69px;top:345px"><div class="icon abs" role="img" aria-label="Compass icon"><span></span></div><h3>Vastu Shastra</h3><div class="bar abs"></div><p>Lorem ipsum dolor sit amet, consectetur adipiscing elit</p><div class="more abs">Read More</div></div>
  <div class="service abs" style="left:431px;top:345px"><div class="icon abs" role="img" aria-label="Footprints icon"><span></span></div><h3>Birth Journal</h3><div class="bar abs"></div><p>Lorem ipsum dolor sit amet, consectetur adipiscing elit</p><div class="more abs">Read More</div></div>
  <div class="service abs" style="left:790px;top:345px"><div class="icon abs" role="img" aria-label="Rings icon"><span></span></div><h3>Manglik Dosha</h3><div class="bar abs"></div><p>Lorem ipsum dolor sit amet, consectetur adipiscing elit</p><div class="more abs">Read More</div></div>
  <div class="service abs" style="left:69px;top:568px"><div class="icon abs" role="img" aria-label="Crystal ball icon"><span></span></div><h3>Crystal Ball</h3><div class="bar abs"></div><p>Lorem ipsum dolor sit amet, consectetur adipiscing elit</p><div class="more abs">Read More</div></div>
  <div class="service abs" style="left:431px;top:568px"><div class="icon abs" role="img" aria-label="Star in circle icon"><span></span></div><h3>Kundli Dosh</h3><div class="bar abs"></div><p>Lorem ipsum dolor sit amet, consectetur adipiscing elit</p><div class="more abs">Read More</div></div>
  <div class="service abs" style="left:790px;top:568px"><div class="icon abs" role="img" aria-label="Tarot cards icon"><span></span></div><h3>Tarot Reading</h3><div class="bar abs"></div><p>Lorem ipsum dolor sit amet, consectetur adipiscing elit</p><div class="more abs">Read More</div></div>
</section>

<!-- Reviews -->
<div class="eyebrow abs center" style="top:2420px">Reviews</div>
<h2 class="section-title abs center" style="top:2441px">What Our Customers Say</h2>
<div class="rule abs" style="top:2523px"></div>
<p class="lead abs" style="top:2565px">Lorem ipsum dolor sit amet, consectetur adipiscing elit. Etiam ullamcorper ut nibh eu lacinia. Maecenas lobortis convallis justo, at ultricies massa. Nunc quam diam, cursus eleifend gravida ac, ornare sit amet risus.</p>

<div class="arrow light abs" style="left:68px;top:2790px"><svg width="10" height="10" viewBox="0 0 10 10"><path d="M6.5 1.5 3 5l3.5 3.5" fill="none" stroke="#0b1a2f" stroke-width="1.8"/></svg></div>
<div class="arrow cream abs" style="left:1100px;top:2790px"><svg width="10" height="10" viewBox="0 0 10 10"><path d="M3.5 1.5 7 5 3.5 8.5" fill="none" stroke="#0b1a2f" stroke-width="1.8"/></svg></div>

<div class="review abs" style="left:153px;top:2672px"><p>Lorem ipsum dolor sit amet, consectetur adipiscing elit. Aenean commodo ligula eget dolor. Aenean massa. Cum sociis natoque penatibus et magnis.</p><div class="avatar abs" role="img" aria-label="Customer portrait"></div><div class="quote abs">“</div><div class="name abs">Jonah Marsh</div><div class="role abs">Astrologer</div></div>
<div class="review abs" style="left:458px;top:2672px"><p>Lorem ipsum dolor sit amet, consectetur adipiscing elit. Aenean commodo ligula eget dolor. Aenean massa. Cum sociis natoque penatibus et magnis.</p><div class="avatar abs" role="img" aria-label="Customer portrait"></div><div class="quote abs">“</div><div class="name abs">Della Finch</div><div class="role abs">Astrologer</div></div>
<div class="review abs" style="left:762px;top:2672px"><p>Lorem ipsum dolor sit amet, consectetur adipiscing elit. Aenean commodo ligula eget dolor. Aenean massa. Cum sociis natoque penatibus et magnis.</p><div class="avatar abs" role="img" aria-label="Customer portrait"></div><div class="quote abs">“</div><div class="name abs">Stella Kingsley</div><div class="role abs">Astrologer</div></div>

<!-- Call to action -->
<section class="cta abs" role="img" aria-label="Starry night sky with a large ringed planet on the right"></section>
<div class="eyebrow abs center" style="top:3188px">Willow Tide Astrology</div>
<h2 class="cta-title abs center">A Personalized Guide Through<br>An Online Astrologer</h2>
<div class="btn cta-btn abs">Book An Appointment</div>

<!-- Blogs -->
<div class="eyebrow abs center" style="top:3663px">News &amp; Updates</div>
<h2 class="section-title abs center" style="top:3684px">Our Latest Blogs</h2>
<div class="rule abs" style="top:3768px"></div>
<p class="lead abs" style="top:3810px">Lorem ipsum dolor sit amet, consectetur adipiscing elit. Etiam ullamcorper ut nibh eu lacinia. Maecenas lobortis convallis justo, at ultricies massa. Nunc quam diam, cursus eleifend gravida ac, ornare sit amet risus.</p>

<div class="arrow light abs" style="left:68px;top:4123px"><svg width="10" height="10" viewBox="0 0 10 10"><path d="M6.5 1.5 3 5l3.5 3.5" fill="none" stroke="#0b1a2f" stroke-width="1.8"/></svg></div>
<div class="arrow cream abs" style="left:1100px;top:4123px"><svg width="10" height="10" viewBox="0 0 10 10"><path d="M3.5 1.5 7 5 3.5 8.5" fill="none" stroke="#0b1a2f" stroke-width="1.8"/></svg></div>

<article class="blog abs" style="left:153px;top:3908px">
  <div class="photo abs" role="img" aria-label="Hand over a glowing zodiac wheel and numbers" style="background:radial-gradient(circle at 55% 35%,#6a4bd6 0%,#3a2a8a 40%,#1a1440 100%)"></div>
  <div class="date abs"><svg width="9" height="9" viewBox="0 0 9 9"><rect x=".5" y="1.5" width="8" height="7" fill="none" stroke="#0b1a2f"/><path d="M.5 3.5h8" stroke="#0b1a2f"/></svg>Feb 20, 2023</div>
  <h3>Lorem ipsum dolor sit elit, slit tetur elit dol dolor</h3>
  <p>Lorem ipsum dolor sit amet, consec tetur adipiscing elit, sed do eiusmod tempor incididunt ut</p>
  <div class="btn read abs">Read More</div>
</article>
<article class="blog abs" style="left:461px;top:3908px">
  <div class="photo abs" role="img" aria-label="Tarot cards beside a stack of old books" style="background:radial-gradient(circle at 45% 45%,#8a6a3a 0%,#4a3328 35%,#1a1722 100%)"></div>
  <div class="date abs"><svg width="9" height="9" viewBox="0 0 9 9"><rect x=".5" y="1.5" width="8" height="7" fill="none" stroke="#0b1a2f"/><path d="M.5 3.5h8" stroke="#0b1a2f"/></svg>Feb 20, 2023</div>
  <h3>Lorem ipsum dolor sit elit, slit tetur elit dol dolor</h3>
  <p>Lorem ipsum dolor sit amet, consec tetur adipiscing elit, sed do eiusmod tempor incididunt ut</p>
  <div class="btn read abs">Read More</div>
</article>
<article class="blog abs" style="left:768px;top:3908px">
  <div class="photo abs" role="img" aria-label="Neon zodiac circle on a violet background" style="background:linear-gradient(90deg,#b1236e 0%,#4d2a9a 35%,#2a2a8a 70%,#1b1f5a 100%)"></div>
  <div class="date abs"><svg width="9" height="9" viewBox="0 0 9 9"><rect x=".5" y="1.5" width="8" height="7" fill="none" stroke="#0b1a2f"/><path d="M.5 3.5h8" stroke="#0b1a2f"/></svg>Feb 20, 2023</div>
  <h3>Lorem ipsum dolor sit elit, slit tetur elit dol dolor</h3>
  <p>Lorem ipsum dolor sit amet, consec tetur adipiscing elit, sed do eiusmod tempor incididunt ut</p>
  <div class="btn read abs">Read More</div>
</article>

<!-- Footer -->
<footer class="footer abs"></footer>
<div class="f-logo abs">Willow Tide Astrology</div>
<p class="f-text abs">Lorem ipsum dolor sit amet, consectetur adipiscing elit, sed do eiusmod tempor incididunt ut labore et dolore magna aliqua. Quis ipsum suspendisse ultrices gravida.</p>
<div class="social abs" aria-label="Social links"><span></span><span></span><span></span><span></span></div>

<h3 class="f-head abs" style="left:397px">Quick Links</h3>
<ul class="f-links abs"><li>About</li><li>Readings</li><li>Booking</li><li>Blog</li><li>Contact</li></ul>

<h3 class="f-head abs" style="left:572px">Contact Us</h3>
<div class="c-row abs" style="top:4680px"><div class="c-icon"><svg width="10" height="10" viewBox="0 0 10 10"><path d="M2 1l2 2-1 1.2c.6 1.3 1.5 2.2 2.8 2.8L7 6l2 2-1.3 1.3C4.5 9 1 5.5.7 2.3z" fill="#f6efa8"/></svg></div><div>CALL US<br>0198 765 432</div></div>
<div class="c-row abs" style="top:4728px"><div class="c-icon"><svg width="10" height="8" viewBox="0 0 10 8"><rect width="10" height="8" fill="#f6efa8"/><path d="M0 0l5 4 5-4" fill="none" stroke="#1d3a63"/></svg></div><div>EMAIL US<br>hello@willowtide.example</div></div>
<div class="c-row abs" style="top:4776px"><div class="c-icon"><svg width="8" height="11" viewBox="0 0 8 11"><path d="M4 0a4 4 0 0 1 4 4c0 3-4 7-4 7S0 7 0 4a4 4 0 0 1 4-4z" fill="#f6efa8"/><circle cx="4" cy="4" r="1.4" fill="#1d3a63"/></svg></div><div>Addres line dummy here<br>Addres line dummy</div></div>

<div class="newsletter abs">
  <h3>Newsletter</h3>
  <p>Subscribe our newsletter to get the latest news.</p>
  <div class="news-field abs"><span>Enter Your Email Here...</span><b><svg width="26" height="10" viewBox="0 0 26 10"><path d="M0 5h24M19 1l4 4-4 4" fill="none" stroke="#0b1a2f" stroke-width="1.8"/></svg></b></div>
</div>
<div class="copy abs">Copyright © 2024 All Rights Reserved By Willow Tide</div>

</body>
</html>
```